need a Flyer for Plush Toy company

Need a Flyer for Plush Toy company ,

I upload a file for TEXT

Target Market(s)

Toys wholesalers , Supermarket

Industry/Entity Type

Toy Store

Colors
000000
ec1f27
c4c4c4

Requirements
Must have
• I have up loaded 3 files
• 1. Logo Registered Brand
• 2. customer's design in drawing
• 3. our ready samples based on Design
Nice to have
• happy kids in Nature ,
• happy kids in Ski ,
• different color Kids ,
• Multi culture concept

```html
<!DOCTYPE html>
<html lang="en">
<head>
<meta charset="utf-8">
<title>Lumo Kasi – Plush Toys Flyer</title>
<link href="https://fonts.googleapis.com/css2?family=Carlito:wght@400;700&display=swap" rel="stylesheet">
<style>
  :root {
    --black: #000000;
    --red: #ec1f27;
    --grey: #c4c4c4;
    --white: #ffffff;
    --ink: #111111;
    --sofa: #a6d49a;
    --kids: #f0c9a8;
    --toys: #f2d070;
  }
  * { margin: 0; padding: 0; box-sizing: border-box; }
  html, body { width: 800px; height: 1200px; overflow: hidden; background: var(--white); }
  body { font-family: "Carlito", "Calibri", sans-serif; color: var(--ink); }
  .flyer { position: relative; width: 800px; height: 1200px; background: var(--white); overflow: hidden; }

  .brand-mark { position: absolute; left: 44px; top: 110px; display: flex; align-items: center; gap: 10px; }
  .brand-mark__dot { width: 22px; height: 22px; border-radius: 50%; background: var(--red); }
  .brand-mark__name { font-weight: 700; font-size: 34px; color: var(--black); }

  .masthead { position: absolute; left: 290px; top: 14px; width: 500px; text-align: center; }
  .masthead__title { font-weight: 700; font-size: 62px; line-height: 1; margin-left: -40px; }
  .masthead__type { font-size: 31px; margin-top: 8px; }
  .masthead__role { font-size: 25px; margin-top: 4px; margin-left: -40px; }
  .masthead__role--small { font-size: 22px; margin-left: -80px; }

  .wave { position: absolute; left: 0; top: 200px; }

  .hero { position: absolute; left: 0; top: 270px; width: 800px; height: 258px; background: var(--grey); }
  .art { position: absolute; }
  .art--kids { left: 19px; top: 292px; width: 230px; height: 222px; border-radius: 50%;
    background: radial-gradient(circle, var(--kids), #b08060 70%, transparent 72%); }
  .art--sofa { left: 286px; top: 335px; width: 490px; height: 258px; border-radius: 14px 14px 4px 4px;
    background: linear-gradient(180deg, #f3e1ec 0%, #d9e3ef 30%, var(--sofa) 45%, #8ec283 100%); }

  .copy { position: absolute; left: 24px; top: 608px; width: 760px; font-weight: 700; font-size: 20px; line-height: 28px; }
  .copy p { margin-bottom: 14px; }
  .copy .accent { color: var(--red); }
  .copy .indent { padding-left: 5px; }

  .contact-band { position: absolute; left: 0; top: 923px; width: 800px; height: 134px; background: var(--grey); }
  .footer-band { position: absolute; left: 0; top: 1056px; width: 800px; height: 144px; background: var(--black); }
  .art--toys { left: 0; top: 938px; width: 452px; height: 175px; border-radius: 40px;
    background: linear-gradient(90deg, #f3a9c6, #f6f2ea 25%, #f39a3c 40%, #b9a8e0 60%, #7fb4e0 75%, var(--toys) 90%); }

  .contact { position: absolute; left: 464px; top: 932px; font-weight: 700; font-size: 18px; line-height: 24px; color: var(--ink); }
  .bank { position: absolute; left: 464px; top: 1062px; font-weight: 700; font-size: 20px; line-height: 26px; color: var(--white); }
  .address { position: absolute; left: 103px; top: 1109px; font-weight: 700; font-size: 27px; line-height: 36px; color: var(--white); }
</style>
</head>
<body>
<div class="flyer">
  <div class="brand-mark"><span class="brand-mark__dot"></span><span class="brand-mark__name">Lumo Kasi</span></div>

  <header class="masthead">
    <h1 class="masthead__title">Lumo Kasi</h1>
    <div class="masthead__type">Einzelunternehmen / Family Business</div>
    <div class="masthead__role">International Trader for Toys</div>
    <div class="masthead__role masthead__role--small">Innovative Developer&nbsp; for Plush Toys</div>
  </header>

  <div class="hero"></div>
  <svg class="wave" width="800" height="80" viewBox="0 0 800 80" aria-hidden="true">
    <path d="M0 40 C200 20 420 0 560 20 C680 36 760 40 800 45 L800 80 L0 80 Z" fill="var(--white)" opacity="0"/>
    <path d="M0 46 C180 30 420 -2 580 14 C680 24 760 32 800 38 L800 62 C760 50 680 42 580 34 C420 22 200 50 0 72 Z" fill="var(--red)"/>
    <path d="M0 44 C180 28 420 -4 580 12 C680 22 760 30 800 36 L800 44 C760 38 680 30 580 22 C420 8 200 38 0 58 Z" fill="var(--black)"/>
    <path d="M0 72 C200 50 420 22 580 34 C680 42 760 50 800 62 L800 80 L0 80 Z" fill="var(--grey)"/>
  </svg>

  <div class="art art--kids" role="img" aria-label="Illustration of children of different cultures holding hands in a circle"></div>
  <div class="art art--sofa" role="img" aria-label="Illustration of six cartoon plush animals sitting on a green sofa"></div>

  <section class="copy">
    <p>We live and work in Bergheim near to Cologne Germany. We speak German and English.</p>
    <p>The toys are made in China, we are small family business , but we are professional in Plush toys business , right now we have successfully&nbsp; launched Projects with a huge Japanese 100 Yen Chain Store.&nbsp; Here in Flyer we show a Sample project.</p>
    <p><span class="accent">100 Yen = 0.90 USD</span>&nbsp; , Our products can meet strictest Quality Control , but are with extremely Low Price to fit for&nbsp; Japanese Dollar Shop as well as his overseas Store around the world.</p>
    <p class="indent">Of course our products are fit for&nbsp; <span class="accent">Premium Store</span> too.</p>
  </section>

  <div class="contact-band"></div>
  <div class="footer-band"></div>
  <div class="art art--toys" role="img" aria-label="Photo of the finished plush toy samples"></div>

  <address class="contact" style="font-style:normal">
    hello@lumokasi.example<br>
    Fon&nbsp;&nbsp; +49 (0)&nbsp; 2271- 400 1180<br>
    Fax&nbsp;&nbsp; +49 (0)&nbsp; 2271- 400 1181<br>
    Mobil:&nbsp; +49 (0) 151 0000 4321<br>
    Ust-IdNr./VAT No. DE000123456
  </address>

  <div class="bank">
    Bank information:<br>
    Kontoinhaber/Account Holder:<br>
    Mei Lorenz<br>
    IBAN:&nbsp; DE00 1234 5678 9012 3456 78<br>
    BIC : XXXXDEFF000
  </div>

  <address class="address" style="font-style:normal">
    Amselweg 7, 50129<br>
    Bergheim Germany
  </address>
</div>
</body>
</html>
```